2m x 3m Trade Show Booth Design

We have a Hospitality Trade Show with a 2m x 3m spot. Two side walls of 2m and one back wall of 3m. Need artwork to be printed on vinyl and attached. Please see attached docs for existing media, logos, etc

```html
<!DOCTYPE html>
<html lang="en">
<head>
<meta charset="utf-8">
<title>VenueMedic Trade Show Booth Walls</title>
<link href="https://fonts.googleapis.com/css2?family=Poppins:ital,wght@0,400;0,600;0,700;1,400;1,600;1,700;1,800&display=swap" rel="stylesheet">
<style>
  :root {
    --stage: #bdbdbd;
    --navy: #1b3a72;
    --blue: #0e5fa8;
    --blue-deep: #14468e;
    --blue-band: #1a4b98;
    --teal: #29b0b5;
    --white: #ffffff;
  }
  * { box-sizing: border-box; margin: 0; padding: 0; }
  html, body { width: 1200px; height: 687px; overflow: hidden; }
  body {
    background: var(--stage);
    font-family: "Poppins", sans-serif;
    position: relative;
  }
  .wall {
    position: absolute;
    top: 85px;
    height: 428px;
    overflow: hidden;
    box-shadow: 0 10px 14px rgba(0,0,0,0.22);
    background: linear-gradient(160deg, var(--blue-deep) 0%, var(--blue) 70%, var(--blue-deep) 100%);
  }
  .wall--left { left: 61px; width: 286px; }
  .wall--back { left: 384px; width: 428px; background: var(--blue); }
  .wall--right { left: 854px; width: 286px; }

  .side-header { position: absolute; inset: 0 0 auto 0; height: 100px; }
  .brand-name {
    position: absolute;
    font-weight: 600;
    color: var(--navy);
    letter-spacing: -1px;
    white-space: nowrap;
  }
  .side-header .brand-name {
    top: 20px; left: 0; right: 0; text-align: center;
    font-size: 31px;
  }

  .side-title {
    position: absolute; left: 26px; right: 20px; top: 100px;
    color: var(--white);
    font-style: italic; font-weight: 800;
    font-size: 24px; line-height: 30px;
  }
  .side-sub {
    position: absolute; left: 26px; top: 170px;
    color: var(--teal);
    font-style: italic; font-weight: 400;
    font-size: 21.5px; line-height: 26px;
  }
  .van-art {
    position: absolute; left: 27px; top: 243px; width: 233px; height: 108px;
    border-radius: 14px 40px 10px 10px;
    background: linear-gradient(90deg, #1b63ad 0%, #1f6cb3 45%, #e4e6ea 62%, #f1f2f4 100%);
  }
  .footer-band {
    position: absolute; left: 0; right: 0; top: 351px; height: 44px;
    background: var(--teal);
    display: flex; align-items: center; justify-content: center; gap: 7px;
    color: var(--white); font-weight: 600; font-size: 12.5px; letter-spacing: 0.2px;
  }
  .footer-base {
    position: absolute; left: 0; right: 0; top: 395px; bottom: 0;
    background: linear-gradient(180deg, #153f8a, var(--blue-band));
  }

  .service-list { position: absolute; left: 24px; top: 182px; list-style: none; }
  .service-item {
    display: flex; align-items: center; gap: 10px;
    height: 41.5px;
    color: var(--white); font-style: italic; font-weight: 600; font-size: 13.5px;
  }
  .service-icon {
    width: 29px; height: 29px; border-radius: 50%;
    background: var(--white); border: 3px solid var(--teal);
    display: flex; align-items: center; justify-content: center; flex: none;
  }

  .back-bg { position: absolute; inset: 0; }
  .wall--back .brand-name {
    left: 25px; top: 36px;
    font-size: 50px; line-height: 50px; letter-spacing: -1.5px;
  }
  .back-tagline {
    position: absolute; left: 26px; top: 112px;
    color: var(--blue); font-weight: 700; font-size: 23px; line-height: 29px;
  }
  .back-promise {
    position: absolute; left: 26px; top: 184px;
    color: var(--navy); font-weight: 700; font-size: 23px; line-height: 29px;
  }
  .social-row { position: absolute; left: 30px; top: 316px; display: flex; gap: 5px; }
  .social-dot { width: 15px; height: 15px; border: 2px solid var(--white); border-radius: 50%; }
  .mascot-art {
    position: absolute; left: 262px; top: 98px; width: 156px; height: 254px;
    border-radius: 70px 70px 16px 16px;
    background: linear-gradient(180deg, #2aa3a5 0%, #3bb3ac 55%, #2b8f96 100%);
  }
  .web-band {
    position: absolute; left: 0; right: 0; top: 352px; bottom: 0;
    background: linear-gradient(180deg, #1a4b98, #0e5fa8 60%);
    display: flex; align-items: center; gap: 17px; padding-left: 31px;
  }
  .web-mark { width: 27px; height: 27px; border-radius: 50%; background: var(--teal); flex: none; }
  .web-address { color: var(--white); font-weight: 600; font-size: 30px; letter-spacing: -0.3px; white-space: nowrap; }
</style>
</head>
<body>

<section class="wall wall--left">
  <svg class="side-header" viewBox="0 0 286 100" preserveAspectRatio="none">
    <path d="M0 0 H286 V71 Q143 122 0 71 Z" fill="var(--teal)"/>
    <path d="M0 0 H286 V59 Q143 107 0 59 Z" fill="var(--white)"/>
  </svg>
  <div class="side-header"><span class="brand-name">VenueMedic</span></div>
  <h2 class="side-title">Reliable specialist support</h2>
  <p class="side-sub">when your venue<br>needs it most.</p>
  <div class="van-art" role="img" aria-label="Illustration of a branded service van with the technician mascot on its side"></div>
  <div class="footer-band">
    <svg width="12" height="15" viewBox="0 0 12 15"><path d="M6 1a4.5 4.5 0 0 0-4.5 4.5C1.5 9 6 13 6 13s4.5-4 4.5-7.5A4.5 4.5 0 0 0 6 1z" fill="none" stroke="#fff" stroke-width="1.8"/><circle cx="6" cy="5.5" r="1.5" fill="#fff"/><line x1="2" y1="14" x2="10" y2="14" stroke="#fff" stroke-width="1.4"/></svg>
    ON-SITE TROUBLESHOOTING
  </div>
  <div class="footer-base"></div>
</section>

<section class="wall wall--back">
  <svg class="back-bg" viewBox="0 0 428 428">
    <rect width="428" height="428" fill="var(--blue)"/>
    <ellipse cx="130" cy="10" rx="270" ry="310" fill="var(--navy)"/>
    <ellipse cx="111" cy="9" rx="255" ry="302" fill="var(--white)"/>
  </svg>
  <span class="brand-name">VenueMedic</span>
  <p class="back-tagline">YOUR HOSPITALITY<br>TECH DOCTOR.</p>
  <p class="back-promise">FAST. LOCAL.<br>RELIABLE.</p>
  <div class="social-row"><span class="social-dot"></span><span class="social-dot"></span><span class="social-dot"></span></div>
  <div class="mascot-art" role="img" aria-label="Illustrated technician mascot in a teal cap and jacket holding a payment terminal"></div>
  <div class="web-band">
    <span class="web-mark"></span>
    <span class="web-address">venuemedic.com.au</span>
  </div>
</section>

<section class="wall wall--right">
  <svg class="side-header" viewBox="0 0 286 100" preserveAspectRatio="none">
    <path d="M0 0 H286 V71 Q143 122 0 71 Z" fill="var(--teal)"/>
    <path d="M0 0 H286 V59 Q143 107 0 59 Z" fill="var(--white)"/>
  </svg>
  <div class="side-header"><span class="brand-name">VenueMedic</span></div>
  <h2 class="side-title">Hardware Issue or Supplies Needed?</h2>
  <ul class="service-list">
    <li class="service-item">
      <span class="service-icon"><svg width="13" height="15" viewBox="0 0 13 15"><rect x="2" y="1" width="9" height="13" rx="1.5" fill="none" stroke="var(--blue)" stroke-width="1.4"/><rect x="4" y="3" width="5" height="3" fill="none" stroke="var(--blue)" stroke-width="1"/></svg></span>
      POS &amp; EFTPOS SUPPORT
    </li>
    <li class="service-item">
      <span class="service-icon"><svg width="15" height="13" viewBox="0 0 15 13"><path d="M1 5a9 9 0 0 1 13 0M3.5 7.5a5.5 5.5 0 0 1 8 0M5.8 9.8a2.3 2.3 0 0 1 3.4 0" fill="none" stroke="var(--blue)" stroke-width="1.3"/><circle cx="7.5" cy="11.5" r="1" fill="var(--blue)"/></svg></span>
      NETWORK &amp; WI-FI REPAIRS
    </li>
    <li class="service-item">
      <span class="service-icon"><svg width="15" height="13" viewBox="0 0 15 13"><rect x="1" y="3" width="13" height="6" rx="1" fill="none" stroke="var(--blue)" stroke-width="1.3"/><path d="M4 9v3h7V9M4 3V1h7v2" fill="none" stroke="var(--blue)" stroke-width="1.3"/></svg></span>
      THERMAL PRINTER FIXES
    </li>
    <li class="service-item">
      <span class="service-icon"><svg width="15" height="13" viewBox="0 0 15 13"><path d="M1 1h13v8H6l-3 3V9H1z" fill="none" stroke="var(--blue)" stroke-width="1.3"/><path d="M4 4h7M4 6.5h5" stroke="var(--blue)" stroke-width="1.1"/></svg></span>
      HOSPITALITY IT CONSULTING
    </li>
  </ul>
  <div class="footer-band">
    <svg width="14" height="14" viewBox="0 0 14 14"><circle cx="7" cy="7" r="6" fill="#fff"/><path d="M4 7.2l2 2 4-4.4" fill="none" stroke="var(--teal)" stroke-width="1.8"/></svg>
    FIXING TODAY. HELPING TOMORROW.
  </div>
  <div class="footer-base"></div>
</section>

</body>
</html>
```